Cortelune Pamphlet

We need to design a pamplet for Cortelune, a Bespoke Wine Cellar design and build company. Our logo and signature cellar should be incorperated into the design (can be seen at www.cortelune-example.com). It should also include what will be called the template with a scematic drawing of a cellar to outline the key features An area called the process will showcase the different types of materials that can be used and there neesa to be indicative costs dependant in size also somewhere, as well as the fact that design £950+VAT but will be taken off the cost of the cellar if we do the job refunded back into project on approval.
.
Updates

Industry/Entity Type

It Company

```html
<!DOCTYPE html>
<html lang="en">
<head>
<meta charset="utf-8">
<title>Cortelune Pamphlet</title>
<link href="https://fonts.googleapis.com/css2?family=Open+Sans:ital,wght@0,400;0,600;0,700;1,700&display=swap" rel="stylesheet">
<style>
:root{
  --canvas:#d8d8d8;
  --wine:#3b0f22;
  --wine-deep:#240511;
  --wine-edge:#4a1a2e;
  --ink-light:#ffffff;
  --ink-dark:#222222;
  --row-light:#e6e6e6;
  --table-bg:#f2f2f2;
}
*{margin:0;padding:0;box-sizing:border-box}
html,body{width:860px;height:1200px;overflow:hidden}
body{background:var(--canvas);font-family:"Open Sans",Arial,sans-serif;position:relative;color:var(--ink-light)}
.abs{position:absolute}

/* inside spread */
.panel-left{left:88px;top:0;width:178px;height:592px;background:linear-gradient(90deg,var(--wine-deep),var(--wine) 60%,var(--wine-edge))}
.panel-right{left:610px;top:6px;width:186px;height:582px;background:linear-gradient(90deg,var(--wine-edge),var(--wine) 40%,var(--wine-deep))}
.hero-cellar{left:266px;top:0;width:344px;height:592px;
  background:linear-gradient(180deg,#eeeeee 0%,#e4e4e4 16%,#c9c6c4 26%,#9a908d 40%,#b5afac 54%,#e9e9e9 64%,#ded6c8 76%,#e6e6e6 86%,#c4c3b3 100%)}

.headline{font-size:17px;line-height:22px;font-weight:400;white-space:nowrap}
.headline em{font-weight:700;font-style:italic}
.headline .r{text-align:right;display:block}
.hl-left{left:108px;top:24px;width:144px}
.hl-left em{font-size:16px;display:block}
.hl-right{left:628px;top:26px;width:148px}

.photo-plans{left:96px;top:128px;width:163px;height:118px;background:linear-gradient(135deg,#efe7da,#cdbda4 55%,#9a8468)}
.photo-craft{left:625px;top:130px;width:162px;height:140px;background:linear-gradient(135deg,#4a3b30,#a0795a 55%,#d3b08a)}

.body-copy{font-size:12px;line-height:14.4px;text-align:justify;hyphens:auto;-webkit-hyphens:auto;letter-spacing:-0.25px}
.body-copy p+p{margin-top:16px}
.copy-left{left:102px;top:297px;width:152px}
.copy-right{left:630px;top:300px;width:150px}

/* back cover */
.cover{background:var(--wine-deep)}
.cover-back{left:64px;top:604px;width:358px;height:558px}
.cover-gallery{left:438px;top:604px;width:362px;height:560px}

.brand{left:96px;top:1000px;width:132px;text-align:center}
.brand-mark{width:28px;height:28px;border:2px solid var(--ink-light);margin:0 auto 22px}
.brand-name{font-size:17px;letter-spacing:3px;font-weight:400}

.contact{left:232px;top:1012px;width:184px;text-align:center;font-size:12.5px;font-weight:600;line-height:20px;white-space:nowrap;font-style:normal}
.contact .web{margin-top:7px}

.tile{border-radius:10px;border:1px solid #d9d0d3}
.tile-1{left:510px;top:625px;width:99px;height:108px;background:linear-gradient(160deg,#3a3a3c,#1d1d20 60%,#6d6860)}
.tile-2{left:632px;top:625px;width:100px;height:108px;background:linear-gradient(160deg,#3c2a1a,#141414 55%,#5a4630)}
.tile-3{left:449px;top:741px;width:101px;height:134px;background:linear-gradient(180deg,#1a5fb0,#3fa0e8 45%,#1b3c88)}
.tile-4{left:571px;top:741px;width:99px;height:134px;background:linear-gradient(180deg,#b89a6a,#3a2a22 35%,#5a1e26 65%,#bdbdbd)}
.tile-5{left:690px;top:741px;width:100px;height:134px;background:linear-gradient(90deg,#cbbfa8,#e8e2d4 40%,#6a4b46 60%,#d9d2c6)}

.cost-table{left:453px;top:891px;width:336px;height:213px;border-radius:20px;overflow:hidden;background:var(--table-bg)}
.cost-title{height:38px;background:linear-gradient(90deg,#b49f84,#d9cbb4,#a89276);font-size:15px;text-align:center;padding-top:10px;color:var(--ink-light)}
.cost-table table{width:100%;border-collapse:collapse;color:var(--ink-dark);font-size:8px;table-layout:fixed}
.cost-table th{font-weight:700;font-size:8.5px;height:16px;text-align:center;background:var(--table-bg)}
.cost-table td{text-align:center;height:32px}
.cost-table tr.light td{background:var(--row-light)}
.cost-table tr.warm td{background:#b9a88e}

.design-note{left:464px;top:1110px;width:312px;text-align:center;font-size:10.5px;font-weight:700;line-height:14px}
</style>
</head>
<body>

<!-- inside spread -->
<section class="abs panel-left"></section>
<div class="abs hero-cellar" role="img" aria-label="Photograph of the signature white wine cellar with racked bottles and wooden crates behind glass doors"></div>
<section class="abs panel-right"></section>

<h2 class="abs headline hl-left">Design<em>starts with an IDEA,</em><span class="r">A Concept</span></h2>
<div class="abs photo-plans" role="img" aria-label="Photograph of rolled architectural plans"></div>
<div class="abs body-copy copy-left">
  <p>We create classic contemporary to bold striking acrylic designs. Every bespoke wine cellar design is unique and individual according to your taste.</p>
  <p>Rich hard wood, hand stitched leather, a spiral wine cellar, beautiful lighting displays and seamless glass finish to display your magnificent collection of wines, champagnes and cigars...</p>
</div>

<h2 class="abs headline hl-right">We take projects<span class="r"><em>to a Journey</em></span><span class="r">from DESIGN to</span><span class="r">BUILD</span></h2>
<div class="abs photo-craft" role="img" aria-label="Photograph of hands shaping a block of wood"></div>
<div class="abs body-copy copy-right">
  <p>The focus behind our collection of cellar designs is that of beauty and originality but for mostly the functionality and precision-engineered preservation through our climate control systems.</p>
  <p>Temperature, humidity, light and bottle orientation are crucial factors in the preservation and the long term storage of vintage wines. This is the main objective throughout all our wine room design and builds.</p>
</div>

<!-- back cover -->
<section class="abs cover cover-back"></section>
<div class="abs brand">
  <div class="brand-mark"></div>
  <div class="brand-name">CORTELUNE</div>
</div>
<address class="abs contact">
  <div>info@cortelune-example.com</div>
  <div>0845 000 7712</div>
  <div class="web">www.cortelune-example.com</div>
</address>

<!-- gallery and costs -->
<section class="abs cover cover-gallery"></section>
<div class="abs tile tile-1" role="img" aria-label="Photograph of a dark wine room with display cabinets"></div>
<div class="abs tile tile-2" role="img" aria-label="Photograph of a lit wine corridor"></div>
<div class="abs tile tile-3" role="img" aria-label="Photograph of a blue lit arched acrylic cellar"></div>
<div class="abs tile tile-4" role="img" aria-label="Photograph of a wine wall with bottle racks"></div>
<div class="abs tile tile-5" role="img" aria-label="Photograph of a cellar doorway with lit shelving"></div>

<div class="abs cost-table">
  <div class="cost-title">Average Construction Costs</div>
  <table>
    <thead><tr><th>Rm. Area</th><th>Capacity</th><th>Build Out</th><th>Racks</th><th>Install</th><th>Cooling</th></tr></thead>
    <tbody>
      <tr class="light"><td></td><td></td><td>0.00£</td><td>0.00£</td><td>0.00£</td><td>0.00£</td></tr>
      <tr class="warm"><td></td><td></td><td>0.00£</td><td>0.00£</td><td>0.00£</td><td>0.00£</td></tr>
      <tr class="light"><td></td><td></td><td>0.00£</td><td>0.00£</td><td>0.00£</td><td>0.00£</td></tr>
      <tr class="warm"><td></td><td></td><td>0.00£</td><td>0.00£</td><td>0.00£</td><td>0.00£</td></tr>
      <tr class="light"><td></td><td></td><td>0.00£</td><td>0.00£</td><td>0.00£</td><td>0.00£</td></tr>
    </tbody>
  </table>
</div>

<p class="abs design-note">The separate price of Cortelune’s cellars designs is £950+VAT. If you leave to us The Construction of our Design you will have The Design for Free.</p>

</body>
</html>
```